Business Card Design Project

I am community manager and social media strategist. I need a double sided business card with company logo and name. Looking for something professional, elegant but also a little bit original.

• - The logo and the colours are the company colours and a required to stay.
- The size should be: 84 x 55 mm (or 3.30 x 2.16)
- The file size should be: 1039 x 697 pixels (300 dpi)
- I'd like rounded corners. :)

Use the following contact information for the card:

Léonie Vardin
Stratégie médias sociaux / community management / édition de sites sociaux
mob. : 0687529103
leonie.vardin@postelune.fr
Twitter. : @lvardin
Skype : vardin.leonie

```html
<!DOCTYPE html>
<html lang="fr">
<head>
<meta charset="utf-8">
<title>NORVANE – Stationery Design</title>
<link rel="stylesheet" href="https://fonts.googleapis.com/css2?family=Source+Sans+3:ital,wght@0,400;0,600;0,700;1,600&display=swap">
<style>
  :root {
    --board-dark: #141414;
    --board-mid: #3b3b3b;
    --white: #ffffff;
    --blue-deep: #0b4f86;
    --blue-main: #1471b3;
    --blue-bright: #2aa0dc;
    --ink-name: #1a5e97;
    --ink-role: #2a8fd0;
    --ink-contact: #164f80;
  }
  * { box-sizing: border-box; margin: 0; padding: 0; }
  html, body { width: 1200px; height: 900px; overflow: hidden; }
  body {
    font-family: "Source Sans 3", sans-serif;
    background:
      linear-gradient(90deg, rgba(255,255,255,0) 0%, rgba(255,255,255,0.08) 45%, rgba(255,255,255,0) 75%),
      linear-gradient(180deg, var(--board-mid) 0%, var(--board-dark) 100%);
    position: relative;
  }
  .board-header { position: absolute; left: 40px; top: 40px; display: flex; align-items: flex-end; gap: 30px; }
  .brand { display: flex; flex-direction: column; align-items: center; gap: 8px; }
  .brand-dot { width: 66px; height: 66px; border-radius: 50%; background: var(--white); }
  .brand-name { color: var(--white); font-weight: 700; font-size: 36px; line-height: 1; letter-spacing: 1px; }
  .board-title { color: var(--white); font-weight: 700; font-size: 32px; line-height: 1; margin-bottom: 2px; }

  .card { position: absolute; top: 216px; width: 420px; height: 640px; border-radius: 32px; overflow: hidden; }
  .card-front {
    left: 256px;
    background:
      radial-gradient(ellipse 140% 70% at 100% 30%, rgba(255,255,255,0.10) 0%, rgba(255,255,255,0) 60%),
      linear-gradient(180deg, #1b74b2 0%, var(--blue-deep) 100%);
    display: flex; flex-direction: column; align-items: center;
  }
  .front-dot { margin-top: 226px; width: 110px; height: 110px; border-radius: 50%; background: var(--white); }
  .front-name { margin-top: 26px; color: var(--white); font-weight: 700; font-size: 60px; line-height: 1; letter-spacing: 2px; }

  .card-back { left: 716px; background: var(--white); }
  .card-back svg { position: absolute; inset: 0; }
  .contact { position: absolute; left: 24px; top: 470px; right: 14px; }
  .contact-name { color: var(--ink-name); font-weight: 700; font-size: 28px; line-height: 1.1; }
  .contact-role { color: var(--ink-role); font-weight: 600; font-style: italic; font-size: 14.5px; line-height: 1.35; margin-top: 6px; }
  .contact-lines { margin-top: 6px; }
  .contact-line { color: var(--ink-contact); font-weight: 600; font-size: 12.5px; line-height: 1.6; }
</style>
</head>
<body>
  <header class="board-header">
    <div class="brand">
      <span class="brand-dot"></span>
      <span class="brand-name">NORVANE</span>
    </div>
    <h1 class="board-title">/ Stationery Design</h1>
  </header>

  <section class="card card-front">
    <span class="front-dot"></span>
    <span class="front-name">NORVANE</span>
  </section>

  <section class="card card-back">
    <svg viewBox="0 0 420 640" width="420" height="640" role="img" aria-label="Decorative sweeping wave pattern in blue tones">
      <defs>
        <linearGradient id="wave-fill" x1="0" y1="0" x2="1" y2="1">
          <stop offset="0" stop-color="var(--blue-bright)"/>
          <stop offset="0.55" stop-color="var(--blue-main)"/>
          <stop offset="1" stop-color="var(--blue-deep)"/>
        </linearGradient>
      </defs>
      <path d="M0 0 H420 V300 C300 360 150 420 0 450 Z" fill="url(#wave-fill)"/>
      <path d="M190 640 C290 622 370 592 420 560 V640 Z" fill="url(#wave-fill)"/>
    </svg>
    <div class="contact">
      <p class="contact-name">Léonie Vardin</p>
      <p class="contact-role">Stratégie médias sociaux / community<br>management / édition de sites sociaux</p>
      <div class="contact-lines">
        <p class="contact-line">Mob. : 0687529103 / Mail: leonie.vardin@postelune.fr</p>
        <p class="contact-line">Twitter. : @lvardin / Skype : vardin.leonie</p>
      </div>
    </div>
  </section>
</body>
</html>
```